Design a clean and bold corporate Presentation for Brand New Company

Task Outline
Create corporate presentation

Task Description
Creation of Powerpoint corporate presentation using the content below.

The presentation is 10 slides long.

PLEASE NOTE: THE FULL CONTENT AND STRUCTURE OF THE CORPORATE PRESENTATION ARE INCLUDED IN ATTACHMENT.

Corporate presentation
– structure is as attached in file titled “novaquill Corp Pres”.

We would like a clean, modern presentation with the use of graphics (not photos) to support key points. We need the graphics designed – NOT clip-art, as we aim to use these on the web-site (examples of preferred design below).

novaquill is a new start-up company where we aim to combine the best of recruitment and IT service delivery expertise to:

Offer access to the best possible resources in the UK and Globally, in a range of commercial models that offer cost savings and agility. Using best practice service delivery to assure quality.

Our foundations are outstanding employee satisfaction, and fantastic customer service.

Do’s
- Be bold ! Use clean design graphics to better highlight and explain products and capabilities in the corporate presentation
- Professional, contemporary and clean – our target market are new IT businesses that are web-savvy.
- Use single colour graphics
- Use a consistent theme through-out
- Establish a design that would translate easily to the web
- Establish a design that would translate into a Powerpoint template
- Use Calibri font

Don’ts
- Use generic photos e.g. “smiling IT professional” ;-)
- No cartoon graphics
- Use complex multi-colour graphics
- Use standard Powerpoint clip-art
- Create a large file
- Use animation / transitions

Output
Powerpoint file – 2011 but compatible with 2007

Deadline
+ 1 week from issue.

What is your industry?
IT Recruitment, Consulting, Professional Services

Target Market
• New customers - Our target market are high growth companies with a heavy reliance on IT, 50-250 employees, based in UK.
• Hiring candidates – IT professionals who are potential hiring candidates for our customers.
• Employees – typically graduates who will be looking for their first/second professional role

What design styles do you like that you would like to reflect in the design?
• http://www.qrtv.com/what-we-offer/
• http://www.brindle.io/platform-as-a-service/brindle-sky-harbor
• www.plume.com

Do you have any other info or links you want to share?
- Corporate presentation
- Logo image

Target Market(s)

Target Market

Industry/Entity Type

It Company

Font styles to use
Sans Serif

Colors
34a6d7
faa54b
d2a4cc
85acd3

Requirements
Must have
• Do’s
• - Be bold ! Use clean design graphics to better highlight and explain products and capabilities in the corporate presentation
• - Professional, contemporary and clean – our target market are new IT businesses that are web-savvy.
• - Use single colour graphics
• - Use a consistent theme through-out
• - Establish a design that would translate easily to the web
• - Establish a design that would translate into a Powerpoint template
• - Use Calibri font
Nice to have
• Use of transparent background imagery
Should not have
• Don’ts
• - Use generic photos e.g. “smiling IT professional” ;-)
• - No cartoon graphics
• - Use complex multi-colour graphics
• - Use standard Powerpoint clip-art
• - Create a large file
• - Use animation / transitions

```html
<!DOCTYPE html>
<html lang="en">
<head>
<meta charset="UTF-8">
<title>novaquill – Our Mission</title>
<link rel="stylesheet" href="https://fonts.googleapis.com/css2?family=Carlito:wght@400;700&display=swap">
<style>
  :root {
    --navy: #23479a;
    --navy-bar: #22458c;
    --orange: #f58220;
    --text-grey: #4a4a4a;
    --rule: #6f8fc8;
    --sky-light: #e4f0fb;
    --sky-mid: #c6def4;
    --white: #ffffff;
  }
  * { margin: 0; padding: 0; box-sizing: border-box; }
  html, body { width: 1200px; height: 900px; overflow: hidden; background: var(--white); }
  body { font-family: "Carlito", "Calibri", sans-serif; }

  .slide { position: relative; width: 1200px; height: 900px; overflow: hidden; background: var(--white); }

  .backdrop {
    position: absolute; inset: 0;
    background:
      radial-gradient(ellipse 700px 600px at 10% 35%, var(--sky-mid) 0%, rgba(198,222,244,0.4) 45%, rgba(255,255,255,0) 75%),
      radial-gradient(ellipse 600px 400px at 95% 10%, var(--sky-light) 0%, rgba(255,255,255,0) 70%),
      linear-gradient(160deg, var(--sky-light) 0%, var(--white) 65%);
  }

  .slide-title {
    position: absolute; left: 22px; top: 36px;
    font-size: 39px; font-weight: 700; color: var(--navy); letter-spacing: 0.5px;
  }
  .title-rule {
    position: absolute; left: 0; top: 96px; width: 910px; height: 1.5px; background: var(--rule);
  }

  .brand {
    position: absolute; right: 24px; top: 36px;
    display: flex; align-items: center; gap: 10px;
    font-size: 44px; font-weight: 700; color: var(--navy);
  }
  .brand-dot { width: 18px; height: 18px; border-radius: 50%; background: var(--orange); }

  .lead {
    position: absolute; left: 63px; top: 178px;
    font-size: 28.5px; font-weight: 700; color: var(--navy);
  }
  .lead .accent { color: var(--orange); }

  .points { position: absolute; left: 78px; top: 262px; width: 920px; list-style: none; }
  .point {
    position: relative; padding-left: 44px;
    font-size: 25.5px; line-height: 42px; color: var(--text-grey); font-weight: 400;
    margin-bottom: 44px;
  }
  .point::before {
    content: ""; position: absolute; left: 2px; top: 12px;
    width: 18px; height: 18px; border-radius: 50%; background: var(--orange);
  }
  .point strong { color: var(--navy); font-weight: 700; }

  .footer-bar {
    position: absolute; left: 0; bottom: 0; width: 1200px; height: 45px; background: var(--navy-bar);
  }
  .copyright {
    position: absolute; left: 9px; bottom: 8px; font-size: 21px; color: var(--white);
  }
  .page-number {
    position: absolute; left: 1106px; top: 824px; width: 74px; height: 74px; border-radius: 50%;
    background: var(--orange); border: 5px solid var(--white);
    display: flex; align-items: center; justify-content: center;
    font-size: 27px; font-weight: 700; color: var(--white);
  }
</style>
</head>
<body>
<div class="slide">
  <div class="backdrop" role="img" aria-label="Soft light-blue abstract swirl and dot texture background"></div>

  <h1 class="slide-title">OUR MISSION</h1>
  <div class="title-rule"></div>

  <div class="brand"><span>novaquill</span><span class="brand-dot"></span></div>

  <p class="lead">Combine the best of <span class="accent">recruitment and IT service delivery expertise to:</span></p>

  <ul class="points">
    <li class="point">Offer access to the best possible resources in the <strong>UK and Globally</strong>, in a range of commercial models that offer cost savings and agility. Using best practice service delivery to assure quality.</li>
    <li class="point">Our foundations are outstanding employee satisfaction, and fantastic customer service.</li>
  </ul>

  <div class="footer-bar"></div>
  <p class="copyright">Copyright text here</p>
  <div class="page-number">01</div>
</div>
</body>
</html>
```